Brightvale Fluid Systems Corp Business Cards

Business cards to match the logo.

Company is a start up water technology company that has developed a patented system using centrifugal force to separate waste from municipal waste water to produce crystal clear clean water. Product sell starting at 2 million to governments both in the US and international.

Business cards should have a professional look with the target generally engineers.

Target Market(s)

Engineers, Government officials and investors

Industry/Entity Type

Water Treatment

Contact Information for Business Card

Business cards design will be used for 6 to 8 people with job titles. Can use the quote "If there is magic in the planet, it is contained in water." but not required to use quote. Should follow theme of Logo

Font styles to use
Other font styles liked:
• match logo font

Requirements
Nice to have
• Colors to match Logo. Business cards to match style of flow of Logo.
• Emphasis on clean look not a busy look. Clean flowing water.
Should not have
• Pictures of industrial equipment or wastewater

```html
<!DOCTYPE html>
<html lang="en">
<head>
<meta charset="utf-8">
<title>Brightvale Fluid Systems – Business Cards</title>
<link rel="stylesheet" href="https://fonts.googleapis.com/css2?family=Arimo:wght@400;700&display=swap">
<style>
  :root {
    --bg: #e6e8eb;
    --card-white: #f7f8f9;
    --sky: #2aa3d9;
    --sky-deep: #1f8fc6;
    --navy: #0f4f86;
    --ink: #163f66;
    --white: #ffffff;
  }
  * { margin: 0; padding: 0; box-sizing: border-box; }
  html, body {
    width: 1200px; height: 997px; overflow: hidden;
    background: var(--bg);
    font-family: "Arimo", Arial, sans-serif;
  }
  .stage { position: relative; width: 1200px; height: 997px; }
  .card {
    position: absolute; width: 560px; height: 320px;
    border-radius: 18px; overflow: hidden;
    background: var(--card-white);
    box-shadow: 0 10px 28px rgba(0,0,0,.18);
  }
  .card svg.bands { position: absolute; inset: 0; width: 100%; height: 100%; }
  .card-back { left: 80px; top: 100px; }
  .card-front { left: 560px; top: 540px; }

  .quote {
    position: absolute; left: 0; right: 0; top: 34px;
    text-align: center; color: var(--navy);
    font-weight: 700; font-size: 12.5px; letter-spacing: .3px;
    text-transform: uppercase;
  }
  .company-name {
    position: absolute; font-weight: 700; text-transform: uppercase;
    letter-spacing: 2px; line-height: 1.15;
  }
  .card-back .company-name {
    left: 0; right: 0; top: 200px; text-align: center;
    color: var(--white); font-size: 30px;
  }
  .card-front .company-name {
    left: 40px; top: 48px; color: var(--navy); font-size: 26px;
  }
  .holder { position: absolute; left: 48px; top: 218px; color: var(--white); }
  .holder-name { font-weight: 700; font-size: 17px; letter-spacing: .5px; text-transform: uppercase; }
  .holder-title { font-size: 14px; margin: 3px 0 0 48px; }
  .holder-web { font-size: 15px; letter-spacing: 1.2px; margin-top: 12px; }
  .divider {
    position: absolute; left: 300px; top: 170px; width: 1px; height: 120px;
    background: rgba(255,255,255,.75);
  }
  .contact { position: absolute; left: 330px; top: 150px; color: var(--white); font-size: 13px; line-height: 1.4; }
  .contact-address { margin-bottom: 10px; }
  .contact-list { list-style: none; }
  .contact-list li { display: flex; align-items: center; gap: 8px; margin-bottom: 4px; font-size: 14px; }
  .contact-list svg { width: 14px; height: 14px; flex: none; }
</style>
</head>
<body>
<main class="stage">

  <section class="card card-back" aria-label="Business card back">
    <svg class="bands" viewBox="0 0 560 320" preserveAspectRatio="none" aria-hidden="true">
      <defs>
        <linearGradient id="skyBack" x1="0" y1="0" x2="0" y2="1">
          <stop offset="0" stop-color="var(--sky)"/>
          <stop offset="1" stop-color="var(--sky-deep)"/>
        </linearGradient>
      </defs>
      <path d="M0,170 C170,150 300,60 560,50 L560,320 L0,320 Z" fill="var(--navy)"/>
      <path d="M0,182 C180,165 310,78 560,66 L560,320 L0,320 Z" fill="url(#skyBack)"/>
    </svg>
    <p class="quote">If there is magic in the planet, it is contained in water</p>
    <h2 class="company-name">Brightvale Fluid Systems</h2>
  </section>

  <section class="card card-front" aria-label="Business card front">
    <svg class="bands" viewBox="0 0 560 320" preserveAspectRatio="none" aria-hidden="true">
      <defs>
        <linearGradient id="skyFront" x1="0" y1="0" x2="0" y2="1">
          <stop offset="0" stop-color="var(--sky)"/>
          <stop offset="1" stop-color="var(--sky-deep)"/>
        </linearGradient>
      </defs>
      <path d="M0,178 C160,205 330,140 560,108 L560,320 L0,320 Z" fill="var(--navy)"/>
      <path d="M0,192 C170,220 340,156 560,124 L560,320 L0,320 Z" fill="url(#skyFront)"/>
    </svg>
    <h2 class="company-name">Brightvale Fluid Systems</h2>

    <div class="holder">
      <p class="holder-name">Marcus Ellery</p>
      <p class="holder-title">Director</p>
      <p class="holder-web">www.brightvalefluid.com</p>
    </div>

    <span class="divider" aria-hidden="true"></span>

    <address class="contact" style="font-style:normal">
      <p class="contact-address">Level 2, 14 Harbour Lane,<br>Kelston Qld 4120</p>
      <ul class="contact-list">
        <li>
          <svg viewBox="0 0 16 16" aria-hidden="true"><circle cx="8" cy="8" r="8" fill="var(--white)"/><path d="M5 4.5l1.6-.5 1 2-1 .8a5 5 0 0 0 2.6 2.6l.8-1 2 1-.5 1.6c-3.5.2-6.7-3-6.5-6.5z" fill="var(--sky-deep)"/></svg>
          1300 555 019
        </li>
        <li>
          <svg viewBox="0 0 16 16" aria-hidden="true"><circle cx="8" cy="8" r="8" fill="var(--white)"/><path d="M5 4.5l1.6-.5 1 2-1 .8a5 5 0 0 0 2.6 2.6l.8-1 2 1-.5 1.6c-3.5.2-6.7-3-6.5-6.5z" fill="var(--sky-deep)"/></svg>
          +61 7 5550 1847
        </li>
        <li>
          <svg viewBox="0 0 16 16" aria-hidden="true"><circle cx="8" cy="8" r="8" fill="var(--white)"/><rect x="4" y="5.5" width="8" height="5.5" rx=".8" fill="var(--sky-deep)"/><path d="M4.3 5.9L8 8.6l3.7-2.7" fill="none" stroke="var(--white)" stroke-width=".9"/></svg>
          enquiry@brightvalefluid.com
        </li>
      </ul>
    </address>
  </section>

</main>
</body>
</html>
```